International Freight Forwarder need a business card

We need a logo design for a freight forwarding company . We are active in Sea Transportation, Truck transportation, and Air Transportation, The design should be have normal dimensions of a card and should not have cuts and holes in its design (printed design is required - lamination accepted)

The said company is agent and sales representative of 2 other Shipping companies (whose logos, name, and website should also be mentioned on the card)

Industry/Entity Type

Logistics

Contact Information for Business Card

Address is "No.7, 2nd Darvish Kuche-ye-Sarvestani, Tehran, IR
Tel number is +98 21 66342819
Fax number is +98 21 66349527
E-Mail address is info@sarvnamavaran.com
Website is www.sarvnamavaran.com

Open Layer Logos attached as well

Colors
33a6d7
0292cd
0255a3
3276b5
85abd2
85cae6
cee9f5
d5e2ee
ffffff

Requirements
Must have
• Main logo of Sarvnama Varan
• Logo of KDR Shipping Line
• London, United Kingdom
• kdrline.com
• Logo of Coral Tide Shipping
• Dubai, United Arab Emirates
• ctsuae.com
• We require OPEN layer file to be submitted to us upon project selection.
Should not have
• Weird Designs such as cuts to the shape or holes in design.

```html
<!DOCTYPE html>
<html lang="en">
<head>
<meta charset="utf-8">
<title>Sarvnama Varan – Business Card</title>
<link href="https://fonts.googleapis.com/css2?family=Lato:wght@300;400;700;900&display=swap" rel="stylesheet">
<style>
  :root {
    --navy: #0f3f63;
    --navy-line: #3f6a8c;
    --brand-blue: #0255a3;
    --paper: #ffffff;
    --backdrop: #eceef0;
    --ink-soft: #d5e2ee;
  }
  * { box-sizing: border-box; margin: 0; padding: 0; }
  html, body {
    width: 1200px; height: 852px; overflow: hidden;
    background: var(--backdrop);
    font-family: "Lato", Arial, sans-serif;
  }
  .sheet {
    position: relative; width: 1200px; height: 852px;
    display: flex; align-items: center; justify-content: center; gap: 50px;
  }
  .card {
    width: 525px; height: 300px; position: relative; overflow: hidden;
    box-shadow: 0 6px 18px rgba(0,0,0,0.12);
  }

  /* Front */
  .card--front { display: flex; background: var(--paper); }
  .front__brand {
    width: 44%; display: flex; flex-direction: column;
    align-items: center; justify-content: center; gap: 10px; padding: 20px;
  }
  .brand-mark {
    width: 70px; height: 70px; border-radius: 50%;
    border: 3px solid var(--brand-blue);
  }
  .brand-name {
    color: var(--brand-blue); font-weight: 700; font-size: 14px;
    line-height: 1.2; text-align: center;
  }
  .front__details {
    width: 56%; background: var(--navy); color: var(--paper);
    padding: 44px 28px 28px 30px;
  }
  .person__name {
    font-weight: 400; font-size: 19px; letter-spacing: 1px; text-transform: uppercase;
  }
  .person__role { font-size: 11px; font-weight: 300; margin-top: 2px; color: var(--ink-soft); }
  .contact { list-style: none; margin-top: 26px; }
  .contact__row {
    display: flex; align-items: flex-start; gap: 10px;
    font-size: 11px; font-weight: 300; line-height: 1.35; margin-bottom: 6px;
  }
  .contact__icon { width: 12px; height: 12px; flex: none; margin-top: 1px; fill: var(--paper); }

  /* Back */
  .card--back { background: var(--navy); display: flex; align-items: center; }
  .partner {
    flex: 1; height: 100%; display: flex; flex-direction: column;
    align-items: center; justify-content: center; color: var(--paper); text-align: center;
  }
  .divider { width: 1px; height: 62%; background: var(--navy-line); }
  .partner__mark {
    width: 62px; height: 62px; border-radius: 50%; margin-bottom: 12px;
  }
  .partner__mark--solid { background: var(--paper); }
  .partner__mark--ring { border: 2px solid var(--paper); }
  .partner__name {
    font-weight: 900; font-size: 12px; letter-spacing: 1px;
    text-transform: uppercase; line-height: 1.25;
  }
  .partner__name--line { font-weight: 400; font-size: 15px; letter-spacing: 0.5px; text-transform: none; }
  .partner__meta {
    font-size: 9px; font-weight: 300; letter-spacing: 1px;
    text-transform: uppercase; margin-top: 10px; line-height: 1.5; color: var(--ink-soft);
  }
</style>
</head>
<body>
<main class="sheet">

  <section class="card card--front">
    <div class="front__brand">
      <span class="brand-mark"></span>
      <p class="brand-name">Sarvnama Varan<br>International<br>Transport.Co L.L.c</p>
    </div>
    <div class="front__details">
      <h1 class="person__name">Daniel Ashford</h1>
      <p class="person__role">Registrar</p>
      <ul class="contact">
        <li class="contact__row">
          <svg class="contact__icon" viewBox="0 0 12 12"><path d="M2.5 0.5l2 2-1 1.5c.8 1.6 2 2.8 3.5 3.5l1.5-1 2 2-1.3 1.8C5 10 1.8 6.8.7 1.8z"/></svg>
          <span>+98 21 66342819</span>
        </li>
        <li class="contact__row">
          <svg class="contact__icon" viewBox="0 0 12 12"><rect x="3" y="0.5" width="6" height="3"/><rect x="0.5" y="4" width="11" height="5" rx="1"/><rect x="3" y="8" width="6" height="3.5"/></svg>
          <span>+98 21 66349527</span>
        </li>
        <li class="contact__row">
          <svg class="contact__icon" viewBox="0 0 12 12"><path d="M0.5 2.5h11v7h-11z M1 3l5 3.5L11 3" fill="none" stroke="#fff" stroke-width="1.1"/></svg>
          <span>info@sarvnamavaran.com</span>
        </li>
        <li class="contact__row">
          <svg class="contact__icon" viewBox="0 0 12 12"><circle cx="6" cy="6" r="5" fill="none" stroke="#fff" stroke-width="1.1"/><path d="M1 6h10M6 1c-2.5 3-2.5 7 0 10M6 1c2.5 3 2.5 7 0 10" fill="none" stroke="#fff" stroke-width="0.9"/></svg>
          <span>www.sarvnamavaran.com</span>
        </li>
        <li class="contact__row">
          <svg class="contact__icon" viewBox="0 0 12 12"><path d="M6 0.5a4 4 0 0 0-4 4c0 3 4 7 4 7s4-4 4-7a4 4 0 0 0-4-4zm0 5.5a1.5 1.5 0 1 1 0-3 1.5 1.5 0 0 1 0 3z"/></svg>
          <span>No.7, 2nd Darvish Kuche-ye-Sarvestani,<br>Tehran, IR</span>
        </li>
      </ul>
    </div>
  </section>

  <section class="card card--back">
    <div class="partner">
      <span class="partner__mark partner__mark--solid"></span>
      <p class="partner__name">Coral Tide<br>Shipping LLC</p>
      <p class="partner__meta">Dubai, United Arab Emirates<br>www.ctsuae.com</p>
    </div>
    <span class="divider"></span>
    <div class="partner">
      <span class="partner__mark partner__mark--ring"></span>
      <p class="partner__name partner__name--line">KDR Shipping Line Ltd</p>
      <p class="partner__meta">London, United Kingdom<br>www.kdrline.com</p>
    </div>
  </section>

</main>
</body>
</html>
```